Webpage Toggle Button Graphics

We are a webhosting company that sells Hosted Servers (Windows/Linux etc). We have for each service in our catalogue a number of on/off/maybe toggle buttons (not actally buttons, but display). Out current design is not modern enough, and would like a new design for the concept. (current screenshot is attached).
Updates

It seems I need to clarify something.  The ICONS I need are for the Buttons in the attachment marked Anti-virus, File Backup, HIDS, DR.  Not anything else on the page. The New icons do need to fit in with the look and feel of the page, and ideally are smaller (so we can fit more of these ICONS on the page). Thanks              

Industry/Entity Type

It Company

Requirements
Must have
• Generic Button Display, with 4 states- ON (Red/Bad, I have this feature), OFF (Green/Good, I do not have this feature), N/A (greyed out, feature is not available), MAYBE (Blue, I dont have this feature but its not really Red/Bad)
• Prefer a generic version with a single visual cue (dot/button or whatever) and a Text Description (i.e. not a custom ICON for each feature)
• Needs to fit in the space similiar to the screenshot, but Ideally smaller.
• Initial buttons are to be for:
• Anti-Virus (AV)
• Backup (Back)
• Host Intrusion Detection (HIDS)
• Disaster Recovery (DR)
• DDOS (DDOS)
• Can submittions be in the format of the attachment with your designs embedded into the picture to show what it will look like in production. May Icon 1-RED, 2, Green, 3 Blue, 4 - Greyed out.
Nice to have
• Ideally the button/display is generic, and our developers can just add the text for any future buttons

```html
<!DOCTYPE html>
<html lang="en">
<head>
<meta charset="utf-8">
<title>Service Features Table</title>
<link href="https://fonts.googleapis.com/css2?family=Arimo:wght@400;700&display=swap" rel="stylesheet">
<style>
  :root {
    --ink: #222;
    --ink-muted: #333;
    --link: #1f5aa6;
    --row-alt: #edf1f5;
    --rule: #c9dbe9;
    --chip-bg: #f7f9fb;
    --chip-border: #cfd8e0;
    --state-on: #e0201f;
    --state-off: #4fae2c;
    --state-maybe: #2b86d6;
    --state-na: #b5b9bd;
    --na-ink: #9aa0a5;
    --blue-top: #5bb0ec;
    --blue-bottom: #1a78c6;
    --blue-edge: #1566a8;
    --sort: #3a8fd8;
  }
  * { box-sizing: border-box; margin: 0; padding: 0; }
  html, body { width: 1200px; height: 320px; overflow: hidden; background: #fff; }
  body { font-family: "Arimo", Arial, sans-serif; color: var(--ink); position: relative; }

  .table { position: absolute; inset: 0; }
  .col-rule { position: absolute; top: 0; width: 1px; height: 320px; background: var(--rule); }

  .head { position: absolute; font-size: 13px; font-weight: 700; color: var(--ink-muted); white-space: nowrap; letter-spacing: 0.3px; }
  .sort {
    display: inline-block; width: 12px; height: 12px; border-radius: 50%;
    border: 1px solid var(--sort); margin-left: 2px; vertical-align: -1px; position: relative; background: #fff;
  }
  .sort::after {
    content: ""; position: absolute; left: 2px; top: 3px;
    border-left: 3px solid transparent; border-right: 3px solid transparent; border-top: 4px solid var(--sort);
  }

  .row { position: absolute; left: 0; width: 1068px; }
  .row.alt { background: var(--row-alt); }

  .server-icon {
    position: absolute; left: 24px; width: 46px; height: 46px; border-radius: 4px;
    background: linear-gradient(#6cc2f2, #1677c4); box-shadow: inset 0 0 0 1px #0f5f9f;
  }
  .server-icon::before {
    content: ""; position: absolute; left: 15px; top: 8px; width: 16px; height: 30px;
    background: linear-gradient(#f4fbff, #bfe1f7); border: 1px solid #0f5f9f;
  }
  .server-icon::after {
    content: ""; position: absolute; left: 19px; top: 13px; width: 8px; height: 2px; background: #0f5f9f;
    box-shadow: 0 4px 0 #0f5f9f;
  }

  .type { position: absolute; left: 75px; font-size: 14px; }
  .name { position: absolute; left: 247px; font-size: 14px; font-weight: 700; color: var(--link); line-height: 23px; letter-spacing: 0.2px; }
  .code { position: absolute; left: 247px; font-size: 14px; color: var(--ink-muted); }

  .features { position: absolute; left: 528px; display: flex; gap: 6px; }
  .toggle {
    display: flex; align-items: center; gap: 6px; width: 78px; height: 22px; padding-left: 8px;
    border-radius: 11px; background: var(--chip-bg); border: 1px solid var(--chip-border);
    font-size: 11px; font-weight: 700; color: var(--ink-muted); white-space: nowrap;
  }
  .toggle .dot {
    width: 9px; height: 9px; border-radius: 50%; flex: none;
    box-shadow: 0 0 0 2px #fff, 0 0 0 3px currentColor;
  }
  .toggle.on .dot { background: var(--state-on); color: #f2b3b3; }
  .toggle.off .dot { background: var(--state-off); color: #bfe3ae; }
  .toggle.maybe .dot { background: var(--state-maybe); color: #b4d5f2; }
  .toggle.na { background: #f0f1f2; border-color: #dde0e3; color: var(--na-ink); font-weight: 400; }
  .toggle.na .dot { background: var(--state-na); color: #e0e2e4; }

  .tool {
    position: absolute; width: 101px; height: 28px; border-radius: 3px;
    background: linear-gradient(var(--blue-top), var(--blue-bottom));
    border: 1px solid var(--blue-edge); box-shadow: 0 2px 0 #0d4f86;
  }
  .tool svg { position: absolute; left: 5px; top: 4px; }

  .actions {
    position: absolute; left: 947px; width: 108px; height: 30px; border: 1px solid #b9cfe0; border-radius: 3px;
    background: #fff; font-size: 14px; line-height: 28px; padding-left: 11px; color: var(--ink-muted);
  }
  .actions::after {
    content: ""; position: absolute; right: 10px; top: 8px; width: 17px; height: 13px;
    border: 1px solid #8a8a8a; background: linear-gradient(#fafafa, #dcdcdc);
  }
  .actions::before {
    content: ""; position: absolute; right: 15px; top: 13px; z-index: 1;
    border-left: 4px solid transparent; border-right: 4px solid transparent; border-top: 5px solid #222;
  }
</style>
</head>
<body>
<div class="table">
  <div class="head" style="left:19px;top:31px">Service Type<span class="sort"></span></div>
  <div class="head" style="left:247px;top:31px">Service Name<span class="sort"></span></div>
  <div class="head" style="left:528px;top:31px">Settings<span class="sort"></span></div>
  <div class="head" style="left:632px;top:7px">Associated</div>
  <div class="head" style="left:632px;top:31px">Features<span class="sort"></span></div>
  <div class="head" style="left:831px;top:31px">Associated Features</div>
  <div class="head" style="left:1072px;top:18px">Actions</div>

  <div class="row alt" style="top:53px;height:74px">
    <div class="server-icon" style="top:5px"></div>
    <div class="type" style="top:18px">Virtual Managed Server</div>
    <div class="name" style="top:3px">My New Virtual Managed Server<br>#134190</div>
    <div class="code" style="top:52px">MIVMS7738042</div>
    <div class="tool" style="left:527px;top:14px"><svg width="30" height="18" viewBox="0 0 30 18"><g fill="none" stroke="#fff" stroke-width="1.3"><rect x="2" y="5" width="16" height="10"/><path d="M2 10h16M7 5v5M13 10v5"/></g><rect x="19" y="3" width="6" height="6" fill="#fff"/></svg></div>
    <div class="tool" style="left:631px;top:14px"><svg width="30" height="18" viewBox="0 0 30 18"><path d="M4 5h5l2 2h9v10H4z" fill="#fff"/><path d="M12 15V10M9 12l3-3 3 3" stroke="#1a78c6" stroke-width="1.6" fill="none"/></svg></div>
    <div class="tool" style="left:736px;top:14px"><svg width="30" height="18" viewBox="0 0 30 18"><rect x="4" y="3" width="16" height="13" fill="#fff"/><path d="M8 12l6-6M10 6h4v4" stroke="#1a78c6" stroke-width="1.5" fill="none"/></svg></div>
    <div class="tool" style="left:841px;top:14px"><svg width="30" height="18" viewBox="0 0 30 18"><g fill="#fff"><ellipse cx="11" cy="4" rx="7" ry="2.5"/><rect x="4" y="4" width="14" height="11"/></g><path d="M4 8.5q7 3 14 0M4 12q7 3 14 0" stroke="#1a78c6" fill="none"/><path d="M21 6a5 5 0 0 1 0 8" stroke="#fff" stroke-width="1.6" fill="none"/></svg></div>
    <div class="actions" style="top:14px">Actions</div>
  </div>

  <div class="row" style="top:128px;height:62px">
    <div class="server-icon" style="top:8px"></div>
    <div class="type" style="top:12px">Virtual Managed Server</div>
    <div class="name" style="top:8px">Orion_Linux_14_2</div>
    <div class="code" style="top:36px">MIVMS7738035</div>
    <div class="features" style="top:17px">
      <div class="toggle on"><span class="dot"></span>AV</div>
      <div class="toggle off"><span class="dot"></span>Backup</div>
      <div class="toggle maybe"><span class="dot"></span>HIDS</div>
      <div class="toggle na"><span class="dot"></span>DR</div>
      <div class="toggle on"><span class="dot"></span>DDOS</div>
    </div>
    <div class="actions" style="top:14px">Actions</div>
  </div>

  <div class="row alt" style="top:190px;height:62px">
    <div class="server-icon" style="top:8px"></div>
    <div class="type" style="top:14px">Virtual Managed Server</div>
    <div class="name" style="top:10px">Orion_linux_14_1</div>
    <div class="code" style="top:38px">MIVMS7738033</div>
    <div class="features" style="top:19px">
      <div class="toggle off"><span class="dot"></span>AV</div>
      <div class="toggle on"><span class="dot"></span>Backup</div>
      <div class="toggle off"><span class="dot"></span>HIDS</div>
      <div class="toggle maybe"><span class="dot"></span>DR</div>
      <div class="toggle na"><span class="dot"></span>DDOS</div>
    </div>
    <div class="actions" style="top:16px">Actions</div>
  </div>

  <div class="row" style="top:252px;height:62px">
    <div class="server-icon" style="top:9px"></div>
    <div class="type" style="top:14px">Dedicated Server</div>
    <div class="name" style="top:10px">Dedicated Server</div>
    <div class="code" style="top:38px">M2DSR12821001</div>
    <div class="features" style="top:20px">
      <div class="toggle on"><span class="dot"></span>AV</div>
      <div class="toggle maybe"><span class="dot"></span>Backup</div>
      <div class="toggle na"><span class="dot"></span>HIDS</div>
      <div class="toggle on"><span class="dot"></span>DR</div>
      <div class="toggle maybe"><span class="dot"></span>DDOS</div>
    </div>
    <div class="actions" style="top:17px">Actions</div>
  </div>

  <div class="col-rule" style="left:524px"></div>
  <div class="col-rule" style="left:944px"></div>
  <div class="col-rule" style="left:1068px"></div>
</div>
</body>
</html>
```